Driving-coach/trainer who wants to inform about the offer and how I can help people to drive more re

I need a flyer that informs potential customers about my offer.

DL size 210 mm x 99 mm, vertical!

I'm a trainer/coach who helps people to drive a car more relaxed, without fear and more confident.

It's a one to one training. I do train people in their own car. It gets people their freedom back to go where and when they like to go by own car...

Target Market(s)

People (man an woman) who are afraid of driving a car, or are very stressed while driving....

Industry/Entity Type

Life Coaching

Font styles to use
Sans Serif

Colors
acd136

Requirements
Must have
• Page 1:
• -my offer (see text-pdf)
• -three fotos (see attached files "Pixmarra") of people who are satisfied with my offer
• Page 2:
• -advantages in the work with me.
• -contact information
• -and a picture of me (see attached file) next to the contact information or the advantages of my work
• -my logo (see attached file) on Page 1 + 2
• -i like a "clear" and structured layout. "Less is more"

```html
<!DOCTYPE html>
<html lang="de">
<head>
<meta charset="utf-8">
<title>Fahrsicher-Coaching Flyer</title>
<link href="https://fonts.googleapis.com/css2?family=Didact+Gothic&family=Roboto:wght@400;500&family=Roboto+Condensed:wght@700&family=Arimo:wght@700&display=swap" rel="stylesheet">
<style>
  :root {
    --green: #acd136;
    --ink: #1f1f1f;
    --panel-grey: #ebebeb;
    --paper: #ffffff;
    --backdrop: #9a9a9a;
  }
  * { box-sizing: border-box; margin: 0; padding: 0; }
  html, body { width: 1200px; height: 1200px; overflow: hidden; }
  body { background: var(--backdrop); position: relative; font-family: "Roboto", sans-serif; color: var(--ink); }

  .flyer { position: absolute; top: 56px; width: 494px; height: 1048px; background: var(--paper); overflow: hidden; box-shadow: 0 8px 14px rgba(0,0,0,.35); }
  .flyer--front { left: 94px; }
  .flyer--back { left: 614px; }

  .brand { position: absolute; left: 13px; top: 12px; font-family: "Didact Gothic", sans-serif; color: var(--green); }
  .brand__name { font-size: 31px; letter-spacing: 2.5px; line-height: 36px; }
  .brand__tag { font-size: 21px; letter-spacing: 2px; line-height: 26px; margin-top: 2px; }

  .photo { position: absolute; }
  .photo--cabrio { left: 0; top: 96px; width: 494px; height: 278px; background: linear-gradient(120deg, #5c6166 0%, #a8a39b 30%, #c7925a 55%, #d9b389 75%, #8c8a86 100%); }
  .photo--countryside { left: 0; top: 86px; width: 494px; height: 278px; background: linear-gradient(180deg, #4d86c9 0%, #9cc3e8 38%, #4f7a36 48%, #c9b46a 62%, #e0d23a 75%, #b8a261 100%); }
  .photo--portrait { left: 356px; top: 330px; width: 138px; height: 94px; background: linear-gradient(90deg, #d4d4d4, #f2f2f2 55%, #dadada); }

  .tab { position: absolute; background: var(--green); }
  .tab--headline { left: 282px; top: 76px; width: 212px; height: 36px; clip-path: polygon(0 0, 100% 0, 100% 100%, 15% 100%); color: #fff; font-family: "Arimo", sans-serif; font-size: 24px; text-align: right; padding: 4px 22px 0 0; }
  .tab--band { left: 0; top: 76px; width: 210px; height: 34px; clip-path: polygon(0 0, 100% 0, 87% 100%, 0 100%); }
  .tab--portrait { left: 93px; top: 330px; width: 263px; height: 94px; clip-path: polygon(19% 0, 100% 0, 100% 100%, 0 100%); }

  .questions { position: absolute; left: 0; top: 332px; width: 400px; height: 94px; background: var(--green); clip-path: polygon(0 0, 86% 0, 100% 100%, 0 100%); color: #fff; font-family: "Roboto Condensed", sans-serif; font-size: 19px; line-height: 28.5px; padding: 5px 0 0 14px; }

  .headline { position: absolute; left: 14px; font-family: "Arimo", sans-serif; font-size: 28.5px; color: var(--green); }
  .flyer--front .headline--intro { top: 474px; }

  .situations { position: absolute; left: 0; top: 472px; width: 494px; height: 344px; background: var(--panel-grey); padding: 16px 14px 0 14px; }
  .situations__title { font-family: "Roboto Condensed", sans-serif; font-size: 19px; margin-bottom: 16px; }
  .checklist { list-style: none; }
  .checklist li { position: relative; padding-left: 39px; font-size: 16px; line-height: 19.5px; margin-bottom: 8px; }
  .checklist li::before { content: ""; position: absolute; left: 0; top: 4px; width: 15px; height: 15px; border: 1.5px solid var(--green); border-radius: 50%; }
  .checklist li.no-mark::before { display: none; }
  .checklist .accent { color: var(--green); }
  .checklist .link { color: var(--green); text-decoration: underline; }

  .headline--outro { top: 858px; margin-top: -24px; }
  .flyer--front .headline--outro { top: 834px; }

  .steps { position: absolute; left: 0; top: 856px; width: 494px; height: 192px; background: var(--green); color: var(--ink); padding: 10px 14px 0 14px; }
  .steps__title { font-family: "Roboto Condensed", sans-serif; color: #fff; font-size: 19px; margin-bottom: 8px; }
  .steps ol { list-style: none; counter-reset: step; }
  .steps li { counter-increment: step; position: relative; padding-left: 43px; font-size: 16.5px; line-height: 21px; margin-bottom: 5px; }
  .steps li::before { content: counter(step) "."; position: absolute; left: 12px; }

  .flyer--back .headline--benefits { top: 468px; }
  .flyer--back .headline--contact { top: 826px; }

  .contact { position: absolute; left: 0; top: 854px; width: 494px; height: 194px; background: var(--green); color: #fff; text-align: center; padding-top: 22px; font-size: 23px; line-height: 30px; }
  .contact__name { font-family: "Roboto Condensed", sans-serif; font-size: 23px; }
</style>
</head>
<body>

<section class="flyer flyer--front">
  <div class="brand">
    <div class="brand__name">Sabine Marquardt</div>
    <div class="brand__tag">Fahrsicher-Coaching</div>
  </div>
  <div class="photo photo--cabrio" role="img" aria-label="Foto: lächelnde Frau mit grauem Haar am Steuer eines Cabriolets"></div>
  <div class="tab tab--headline">Wollen Sie</div>
  <div class="questions">
    Fahrangst überwinden?<br>
    Panikattacken beim Autofahren loswerden?<br>
    Oder einfach sicher Autofahren?
  </div>
  <h2 class="headline headline--intro">Dann sind Sie hier richtig!</h2>
  <div class="situations">
    <h3 class="situations__title">Kommt Ihnen eine dieser Situationen bekannt vor?</h3>
    <ul class="checklist">
      <li>Angst oder Panikattacken begleiten Sie beim Autofahren. Vielleicht vermeiden Sie deshalb das Autofahren komplett. - Sie möchten <span class="accent">angstfrei und/oder ohne Panikattacken</span> fahren.</li>
      <li>Sie trauen sich das Autofahren nicht (mehr) zu. - Sie wünschen sich, <span class="accent">sicher, entspannt und stressfrei Auto zu fahren</span>.</li>
      <li>Autofahren erleben Sie unter hoher Anspannung und Stress. - Sie wünschen sich, Autofahren <span class="accent">sicher und entspannt</span> zu erleben.</li>
      <li>Bestimmte Situationen (z.B. Autobahn, Baustellen, Stadtvekehr...) bereiten Ihnen großen Stress. - Sie möchten diese Situationen <span class="accent">souveräner</span> meistern.</li>
    </ul>
  </div>
  <h2 class="headline headline--outro">Das muss nicht so bleiben!</h2>
  <div class="steps">
    <h3 class="steps__title">3 Schritte zur Lösung:</h3>
    <ol>
      <li>Erstgespräch vereinbaren</li>
      <li>Analyse Ihrer individuellen Situation und Zielsetzung</li>
      <li>Individuelles Coaching und Training<br>(ggf. Fahrangst-Therapie - als psychotherapeutische Heilpraktikerin bin ich auf Angst- und Panikstörungen spezialisiert)</li>
    </ol>
  </div>
</section>

<section class="flyer flyer--back">
  <div class="brand">
    <div class="brand__name">Sabine Marquardt</div>
    <div class="brand__tag">Fahrsicher-Coaching</div>
  </div>
  <div class="photo photo--countryside" role="img" aria-label="Foto: gelber Kleinwagen mit Koffern auf dem Dach in einer Sommerwiese"></div>
  <div class="tab tab--band"></div>
  <div class="tab tab--portrait"></div>
  <div class="photo photo--portrait" role="img" aria-label="Porträtfoto der Trainerin in weißer Bluse"></div>
  <h2 class="headline headline--benefits">Advantages in the work with me:</h2>
  <div class="situations">
    <h3 class="situations__title">Kommt Ihnen eine dieser Situationen bekannt vor?</h3>
    <ul class="checklist">
      <li>über 10 Jahre Erfahrung als <span class="accent">Trainerin und Coach</span> im Bereich <span class="accent">Fahrsicherheit</span>.</li>
      <li class="no-mark">Als <span class="accent">psychotherapeutische Heilpraktikerin</span> bin ich <span class="accent">auf Angststörungen und Panikattacken spezialisiert</span></li>
      <li><span class="accent">100 % auf Sie zugeschnitten:</span> ich hole Sie genau dort ab, wo Sie jetzt stehen und unterstütze Sie in <span class="accent">Ihrem Prozess individuell und zielführend</span>.</li>
      <li>Wenn es Ihnen nicht möglich ist, in meine Praxis nach Neustadt Süd zu kommen: Mit der <span class="link">mobilen Praxis</span> <span class="accent">komme ich auch zu Ihnen</span>.</li>
      <li><span class="accent">Termine</span> sind auch <span class="accent">abends und am Wochenende möglich.</span></li>
    </ul>
  </div>
  <h2 class="headline headline--contact">Contact:</h2>
  <div class="contact">
    <div class="contact__name">Sabine Marquardt</div>
    <div>Weitere Informationen finden Sie auf:</div>
    <div>www.fahrsicher-coaching.de</div>
    <div>Oder rufen Sie mich einfach an:</div>
    <div>Tel. 0151 23 45 67 89</div>
  </div>
</section>

</body>
</html>
```